SUMMIT GATHERING 2021. August 20th -22nd.

The Hosts of the conference: Grace Tabernacle-Pastors Ron n Della ( Picture with two persons)

Guest Minister: Bishop Lucinda Okotieno. (Cedar Ridge Awakening)

Venue:
Sealand Gateway Lodgeview. 4817 North 239th Avenue Seattle, WA 98174.

Conference times.
Friday August 20th 6pm-8:30pm
Saturday August 21st. 6pm-8:30pm

Sunday August 22nd 10am-1pm
“ CHURCH RENEWAL GATHERING”

5pm-7:30pm
TWOFOLD SURGE GATHERING.

Target Market(s)

18-55

Industry/Entity Type

Religious/ Entertainment.

Requirements
Must have
• A highlight of the Relaunch service on Sunday August 22nd 5pm-7:30pm.
Nice to have
• Excellent ideas….

```html
<!DOCTYPE html>
<html lang="en">
<head>
<meta charset="UTF-8">
<title>Summit Gathering 2021</title>
<link href="https://fonts.googleapis.com/css2?family=Montserrat:ital,wght@0,400;0,600;0,700;0,800;0,900;1,500&family=Great+Vibes&display=swap" rel="stylesheet">
<style>
  :root {
    --backdrop: #e7e2d7;
    --deep-violet: #3a1c8c;
    --indigo: #3f1d94;
    --magenta: #a52a9e;
    --pink: #e9439b;
    --hot-pink: #ea3f94;
    --white: #ffffff;
    --yellow: #f6ea12;
    --logo-dark: #1b1520;
  }
  * { margin: 0; padding: 0; box-sizing: border-box; }
  html, body {
    width: 1200px; height: 900px; overflow: hidden;
    background: var(--backdrop);
    font-family: "Montserrat", sans-serif;
  }
  .flyer {
    position: absolute; left: 296px; top: 20px;
    width: 608px; height: 860px; overflow: hidden;
    background: linear-gradient(160deg, var(--deep-violet) 0%, #6a23a6 40%, var(--magenta) 75%, #8a2aa8 100%);
    color: var(--white);
  }
  .abs { position: absolute; }
  .title-main {
    left: 40px; top: 28px; font-weight: 900; font-size: 112px;
    letter-spacing: -2px; line-height: 1;
    text-shadow: 3px 4px 6px rgba(0,0,0,.35);
  }
  .title-sub {
    left: 62px; top: 140px; font-weight: 800; font-size: 54px; line-height: 1;
    text-shadow: 2px 3px 5px rgba(0,0,0,.3);
  }
  .title-year {
    left: 430px; top: 104px; font-family: "Great Vibes", cursive;
    font-size: 64px; color: var(--yellow); line-height: 1;
  }
  .dates {
    left: 110px; top: 202px; font-weight: 800; font-size: 34px; line-height: 1;
  }
  .dates sup { font-size: 16px; vertical-align: top; position: relative; top: 2px; }
  .venue {
    left: 120px; top: 252px; font-weight: 600; font-size: 15px; line-height: 1.3;
    display: flex; gap: 8px;
  }
  .venue svg { flex: none; margin-top: 3px; }
  .photo-guest {
    left: 70px; top: 340px; width: 170px; height: 260px;
    background: linear-gradient(180deg, #dfe2e6 0%, #c9c9cc 55%, #6e6a6c 100%);
  }
  .photo-hosts {
    left: 380px; top: 300px; width: 228px; height: 270px;
    background: linear-gradient(160deg, #5a1a7a 0%, #b03a8c 45%, #2a1c30 80%, #e5d9e2 100%);
  }
  .logo-block {
    left: 222px; top: 318px; width: 176px; height: 230px;
    background: var(--logo-dark);
    border: 3px solid #c9a45a;
    display: flex; align-items: center; justify-content: center;
    text-align: center;
  }
  .logo-name {
    font-weight: 800; font-size: 22px; line-height: 1.2; color: var(--white);
  }
  .panel { left: 0; top: 0; }
  .person { line-height: 1.2; }
  .person .name { font-weight: 800; font-size: 17px; }
  .person .role { font-weight: 400; font-size: 17px; }
  .person .note { font-style: italic; font-weight: 500; font-size: 12px; }
  .guest { left: 78px; top: 612px; }
  .hosts { left: 378px; top: 568px; }
  .renewal {
    left: 38px; top: 690px; font-weight: 900; font-size: 44px; line-height: .92;
    color: var(--pink);
  }
  .renewal-when {
    left: 40px; top: 820px; font-weight: 800; font-size: 16px;
  }
  .schedule { left: 348px; top: 672px; line-height: 1.25; }
  .schedule h3 { font-weight: 800; font-size: 15px; }
  .schedule p { font-weight: 400; font-size: 15px; }
  .schedule .divider { width: 170px; height: 3px; background: var(--hot-pink); margin: 8px 0 10px; }
</style>
</head>
<body>
  <div class="flyer">
    <div class="abs photo-hosts" role="img" aria-label="Photo of the host pastors, a smiling couple on a pink-lit stage"></div>

    <svg class="abs panel" width="608" height="860" viewBox="0 0 608 860" aria-hidden="true">
      <polygon points="0,610 608,556 608,860 0,860" fill="var(--indigo)"/>
      <polygon points="330,600 560,540 608,600 608,610 330,640" fill="var(--magenta)" opacity=".85"/>
      <line x1="330" y1="612" x2="330" y2="680" stroke="var(--magenta)" stroke-width="2"/>
      <polygon points="430,760 608,724 608,740 430,776" fill="var(--hot-pink)"/>
      <polygon points="320,860 608,800 608,860" fill="var(--hot-pink)"/>
    </svg>

    <div class="abs photo-guest" role="img" aria-label="Portrait photo of the guest minister in a checked jacket"></div>
    <div class="abs logo-block">
      <span class="logo-name">Grace<br>Tabernacle</span>
    </div>

    <div class="abs title-main">SUMMIT</div>
    <div class="abs title-sub">GATHERING</div>
    <div class="abs title-year">2021</div>
    <div class="abs dates">August 20<sup>TH</sup>-22<sup>ND</sup></div>
    <div class="abs venue">
      <svg width="12" height="16" viewBox="0 0 12 16" aria-hidden="true">
        <path d="M6 0C2.7 0 0 2.6 0 5.9 0 10.3 6 16 6 16s6-5.7 6-10.1C12 2.6 9.3 0 6 0z" fill="#fff"/>
        <circle cx="6" cy="6" r="2.3" fill="#7a2aa5"/>
      </svg>
      <span>Sealand Gateway Lodgeview. 4817 North<br>239th Avenue Seattle, WA 98174.</span>
    </div>

    <div class="abs person hosts">
      <div class="name">Pastors Ron n Della</div>
      <div class="role">Grace Tabernacle</div>
      <div class="note">The Hosts Of The Conference</div>
    </div>
    <div class="abs person guest">
      <div class="name">Bishop Lucinda Okotieno</div>
      <div class="role">Cedar Ridge Awakening</div>
      <div class="note">Guest Minister</div>
    </div>

    <div class="abs renewal">CHURCH<br>RENEWAL<br>GATHERING</div>
    <div class="abs renewal-when">Sunday August 22nd 10am-1pm</div>

    <div class="abs schedule">
      <h3>CONFERENCE TIMES.</h3>
      <p>Friday Aug. 20th 6pm-8:30pm</p>
      <p>Saturday Aug. 21st. 6pm-8:30pm</p>
      <div class="divider"></div>
      <h3>TWOFOLD SURGE GATHERING.</h3>
      <p>5pm-7:30pm</p>
    </div>
  </div>
</body>
</html>
```